Communication of Recommended Belief Letter

To Whom This May Concern,

My company's name is Bramwell LLC. I would like to send electronic messages to my clients. Therefore, I would like PixelHarbor to create a letterhead template to say Bramwell- without the LLC. My messages could extend up to 20 pages long. I would like something that is chic, fancy, and has creative designs. The background color should be white. The creative designs are open for suggestions without color restrictions. Font type and color are also open for suggestions. It may be what you believe best suite's the letterhead. I would like the letterhead to include the company logo. Please see attachment for file. Thank you.

Target Market(s)

working class American's

Industry/Entity Type

Communication

Contact Information for Business Card

The business card should be chic and fancy.

Font styles to use
Script

Requirements
Must have
• Company name: Bramwell LLC
• Company symbol: Please see attachment
• Name: Marisol Denby
• Title: President
• Company website: www.bramwellllc-example.com
Nice to have
• Open for suggestions

```html
<!DOCTYPE html>
<html lang="en">
<head>
<meta charset="utf-8">
<title>Bramwell Letterhead</title>
<link href="https://fonts.googleapis.com/css2?family=Arimo:wght@400;700&display=swap" rel="stylesheet">
<style>
  :root {
    --backdrop: #e4e4e2;
    --paper: #f2f2f2;
    --ink: #3a3a3a;
    --ink-soft: #555;
    --gold: #b07a12;
    --gold-light: #d8a450;
    --gold-dark: #8a5c08;
    --signature-ink: #6f7bc2;
  }
  * { box-sizing: border-box; margin: 0; padding: 0; }
  html, body { width: 1200px; height: 1146px; overflow: hidden; }
  body { background: var(--backdrop); font-family: "Arimo", Arial, sans-serif; color: var(--ink); }

  .letterhead {
    position: absolute; left: 170px; top: 16px;
    width: 860px; height: 1114px;
    background: var(--paper);
  }

  .brand { position: absolute; left: 63px; top: 64px; display: flex; align-items: center; gap: 14px; }
  .brand-mark { width: 78px; height: 78px; border-radius: 50%;
    background: radial-gradient(circle at 40% 35%, #f3d36e, var(--gold) 60%, var(--gold-dark)); }
  .brand-text { display: flex; flex-direction: column; }
  .brand-name { font-size: 38px; font-weight: 400; color: var(--gold); letter-spacing: 1px; line-height: 1; }
  .brand-url { font-size: 17px; color: #777; margin-top: 4px; }

  .contact { position: absolute; left: 646px; top: 54px; font-size: 11px; line-height: 14px; color: var(--ink-soft); }
  .contact-person { border-left: 2px solid var(--gold); padding-left: 9px; }
  .contact-name { font-size: 12.5px; font-weight: 700; color: var(--ink); }
  .contact-details { border-left: 1px solid #bbb; padding-left: 10px; margin-top: 10px; }
  .contact-line { display: flex; align-items: center; gap: 5px; }
  .contact-address { margin-top: 4px; }

  .letter-date { position: absolute; left: 62px; top: 303px; font-size: 12px; font-weight: 700; }
  .recipient { position: absolute; left: 62px; top: 332px; font-size: 12px; line-height: 14.8px; font-style: normal; }

  .letter-body { position: absolute; left: 62px; top: 475px; width: 736px; font-size: 11.6px; line-height: 14.8px; }
  .letter-body p { margin-bottom: 14.8px; }

  .closing { position: absolute; left: 62px; top: 800px; font-size: 12px; line-height: 14.8px; }
  .signature { position: absolute; left: 158px; top: 791px; width: 134px; height: 66px;
    background: linear-gradient(135deg, rgba(111,123,194,0.18), rgba(111,123,194,0.35)); border-radius: 4px; }

  .footer-band { position: absolute; left: 0; bottom: 0; height: 15px; width: 644px;
    background: linear-gradient(90deg, var(--gold-dark), #c98f18 30%, var(--gold-dark) 45%, #d9a020 65%, var(--gold-dark)); }
  .footer-accent { position: absolute; right: 0; bottom: 0; height: 15px; width: 210px; background: var(--gold-light); }
</style>
</head>
<body>
  <main class="letterhead">
    <header>
      <div class="brand">
        <div class="brand-mark"></div>
        <div class="brand-text">
          <span class="brand-name">BRAMWELL</span>
          <span class="brand-url">www.bramwellllc-example.com</span>
        </div>
      </div>
      <div class="contact">
        <div class="contact-person">
          <div class="contact-name">Marisol Denby</div>
          <div>President</div>
        </div>
        <div class="contact-details">
          <div class="contact-line">
            <svg width="9" height="9" viewBox="0 0 10 10"><path d="M2 0.5 L4 2.5 L3 4 Q4.5 6 6 7 L7.5 6 L9.5 8 L8 9.5 Q3 9 0.5 2 Z" fill="#b07a12"/></svg>
            +1-555-014-2268
          </div>
          <div class="contact-line">
            <svg width="10" height="8" viewBox="0 0 10 8"><rect x="0" y="0" width="10" height="8" fill="#b07a12"/><path d="M0 0 L5 4.5 L10 0" stroke="#f2f2f2" fill="none" stroke-width="1"/></svg>
            info@bramwellllc-example.com
          </div>
          <div class="contact-address">P.O. Box 2290, Alder Creek<br>Oregon 97011</div>
        </div>
      </div>
    </header>

    <div class="letter-date">30.09.2017</div>
    <address class="recipient">Recipient’s name<br>Lindenweg 14<br>20251 Hamburg<br>Germany</address>

    <section class="letter-body">
      <p>Dear sir,</p>
      <p>Communication is a very integral part of living creatures, animals and humans. Communication may be verbal or written. Written communication however is only applicable to human beings. Can you even imagine a world without communication? Verbal communication can be through telephones, webcams or in person. Written communication is through letters, emails and mobile phone messages.</p>
      <p>In today’s world of great inventions and technology, letters have somehow become redundant. It is the time for text messages or chats. But they still can communicate a lot more than all other modes of communication. Organizations and various government departments still bank on letters as a strong medium of communication. There is no comparison in costs of sending letters as compared to costs of mobile phone messages though – letters are far cheaper. Letters now commonly known as “hard copy documents” are considered more relevant and important than email copies of text messages as proof or evidence of some sort.</p>
      <p>Letters speak volumes about a person or an organization that writes it. So one must take utmost care ensuring that the language used in any letter is appropriate for the occasion for which it is being written. Since a letter is also a written proof or document, if there are certain things that should not form a part of it, then that too should be carefully handled.</p>
      <p>Writing a good letter is an art. But if for some reason someone is unable to write that perfect letter, these different types of letters provide a base for you to build on. Sample letters have been given for everyone to understand what all information needs to form a part of the letter type and then it can be customized.</p>
    </section>

    <div class="closing">Yours Sincerely,<br>Tobin Rauls</div>
    <div class="signature" role="img" aria-label="Handwritten signature of the sender in blue ink"></div>

    <footer>
      <div class="footer-band"></div>
      <div class="footer-accent"></div>
    </footer>
  </main>
</body>
</html>
```